Landing Page that will convert (Design Only Landing Page Project)

I am looking for a design that will resonate with a dentist, doctor or anyone business owner in the medical field. My goal is to have then scheduled a 15 min session with me at the end to discuss how I can help then meet there financial goals (short or long term)

I am open to all design concepts and suggestions as far as the important contents or links that should be on the page (ie. Main menu like, Home, About, Services, Schedule, Contact Us).

There is no right or wrong answer, just need a great accounting/financing landing page. Again the project is for just the design of the page, and coding will be done elsewhere.

Target Market(s)

medical professionals, this includes small business owners of privately held office suck as medical doctors, dentist, ophthalmologist, chiropractors, etc

Industry/Entity Type

Finance And Accounting

Colors
fdfdfd
1b1b1b
f3f1f8
e4daeb

Requirements
Must have
• The goal of this landing page is to have the visitor schedule a 15min discovery call, therefore, a calender scheduling option is ideal, so we can understand their goals and see what obstacles they are facing and therefore avoid those obstacles before they become a burden
Nice to have
• A video background or maybe a medical professional office in that way they feel connected. For design purposes just use a video/image placeholder. I feel more is less if we can research some of the most successful landing page design and incorporate some of those elements that would to great.
• I saw this example and thought it was ok
• https://www.plovanet.com/#features
• WHAT I LIKE ABOUT THIS DESIGN:
• - It's simple, clean,
• - font is readable,
• - like the illustration
• - elegance
• - It clearly defines what the use should do, its intuitive, walks the user to the bottom of the page and give them the option of whether to signup or exit the page.

```html
<!DOCTYPE html>
<html lang="en">
<head>
<meta charset="utf-8">
<title>Meridian Ledger – Schedule a Session</title>
<link href="https://fonts.googleapis.com/css2?family=Montserrat:wght@700&family=Arimo:wght@400;700&display=swap" rel="stylesheet">
<style>
  :root{
    --page-bg:#fbfafc;
    --soft-lilac:#f3f1f8;
    --footer-bg:#3f2557;
    --white:#ffffff;
    --field-border:rgba(255,255,255,.32);
    --field-fill:rgba(255,255,255,.06);
    --field-label:rgba(255,255,255,.62);
    --footer-muted:rgba(255,255,255,.55);
    --footer-faint:rgba(255,255,255,.38);
    --social-line:rgba(255,255,255,.45);
    --button-text:#4a3a5c;
  }
  *{box-sizing:border-box;margin:0;padding:0}
  html,body{width:1200px;height:926px;overflow:hidden;background:var(--page-bg)}
  body{position:relative;font-family:"Arimo",Arial,sans-serif;color:var(--white)}

  .backdrop{position:absolute;left:0;top:0;width:1200px;height:637px}

  .schedule{position:absolute;left:0;top:0;width:1200px;height:637px;text-align:center}
  .schedule__icon{position:absolute;left:566px;top:136px;width:68px;height:68px}
  .schedule__title{position:absolute;left:0;width:1200px;top:218px;font-family:"Montserrat",sans-serif;font-weight:700;font-size:32px;letter-spacing:.2px}
  .schedule__lead{position:absolute;left:320px;width:560px;top:277px;font-size:13px;line-height:21px;color:rgba(255,255,255,.92)}

  .field{position:absolute;width:262px;height:40px;border:1.6px solid var(--field-border);background:var(--field-fill);border-radius:3px;
    font-size:11.5px;font-weight:700;color:var(--field-label);text-align:left;padding:0 0 0 16px;line-height:37px;letter-spacing:.2px}
  .field--active{border-color:var(--white);color:var(--white)}
  .field__icon{position:absolute;right:10px;top:9px;width:21px;height:21px}
  .col-a{left:330px}.col-b{left:608px}
  .row-1{top:344px}.row-2{top:400px}.row-3{top:456px}

  .submit{position:absolute;left:538px;top:511px;width:124px;height:37px;background:var(--white);color:var(--button-text);
    border-radius:2px;font-size:11.5px;font-weight:700;line-height:37px;letter-spacing:.2px;box-shadow:0 6px 16px rgba(60,30,90,.25)}

  .footer{position:absolute;left:0;top:637px;width:1200px;height:289px;background:var(--footer-bg)}
  .brand{position:absolute;left:132px;top:58px;display:flex;align-items:center;gap:9px;font-size:26px;font-weight:400;color:var(--white);letter-spacing:.3px}
  .brand__mark{width:12px;height:12px;border-radius:50%;background:var(--white)}
  .footer__about{position:absolute;left:132px;top:111px;width:300px;font-size:13px;line-height:21px;color:var(--footer-muted)}
  .social{position:absolute;left:132px;top:170px;display:flex;gap:8px}
  .social svg{width:29px;height:33px}
  .copyright{position:absolute;left:131px;top:223px;font-size:11px;color:var(--footer-faint)}

  .links{position:absolute;top:55px}
  .links h3{font-size:14.5px;font-weight:700;color:var(--white);margin-bottom:14px}
  .links ul{list-style:none}
  .links li{font-size:13px;line-height:24px;color:var(--footer-muted);padding-left:1px}
  .links--services{left:528px}.links--company{left:773px}.links--resources{left:966px}
</style>
</head>
<body>

<svg class="backdrop" viewBox="0 0 1200 637" aria-hidden="true">
  <defs>
    <linearGradient id="violetFill" x1="0" y1="0" x2="1" y2="0.35">
      <stop offset="0" stop-color="#5a4572"/>
      <stop offset="0.55" stop-color="#765d93"/>
      <stop offset="1" stop-color="#9a7cb6"/>
    </linearGradient>
    <filter id="softShadow" x="-10%" y="-20%" width="120%" height="140%">
      <feDropShadow dx="0" dy="-4" stdDeviation="14" flood-color="#3f2557" flood-opacity=".12"/>
    </filter>
  </defs>
  <path d="M860 0 Q880 48 960 44 L1200 20 L1200 0 Z" fill="var(--soft-lilac)"/>
  <path filter="url(#softShadow)" d="M0 364 L528 56 Q600 18 672 56 L1200 364 L1200 637 L0 637 Z" fill="url(#violetFill)"/>
</svg>

<main class="schedule">
  <svg class="schedule__icon" viewBox="0 0 68 68" fill="none" stroke="#fff" stroke-width="2.6" stroke-linecap="round" stroke-linejoin="round" aria-hidden="true">
    <rect x="3" y="6" width="62" height="58" rx="5"/>
    <line x1="3" y1="18" x2="65" y2="18"/>
    <line x1="19" y1="1" x2="19" y2="11"/><line x1="49" y1="1" x2="49" y2="11"/>
    <circle cx="16" cy="30" r="3.5"/><circle cx="28" cy="30" r="3.5"/><circle cx="40" cy="30" r="3.5"/><circle cx="52" cy="30" r="3.5"/>
    <circle cx="28" cy="44" r="3.5"/><circle cx="40" cy="44" r="3.5"/><circle cx="52" cy="44" r="3.5"/>
    <circle cx="13" cy="48" r="9" fill="#6a5384"/>
    <polyline points="8.5,48 12,51.5 18,44.5"/>
  </svg>
  <h1 class="schedule__title">Scheduled A 15 Minutes Session</h1>
  <p class="schedule__lead">Lorem ipsum dolor sit amet, consectetur adipiscing elit. Nullam in auctor urna. Maecenas tempus lorem felis, vel mattis nisl viverra sit amet.</p>

  <div class="field field--active col-a row-1">First Name</div>
  <div class="field col-b row-1">Last Name</div>
  <div class="field col-a row-2">Email Addres</div>
  <div class="field col-b row-2">Phone</div>
  <div class="field col-a row-3">Choose Session Date
    <svg class="field__icon" viewBox="0 0 21 21" fill="none" stroke="rgba(255,255,255,.55)" stroke-width="1.2" aria-hidden="true">
      <rect x="1" y="3" width="19" height="17" rx="1.5"/><line x1="1" y1="7" x2="20" y2="7"/>
      <line x1="6" y1="1" x2="6" y2="5"/><line x1="15" y1="1" x2="15" y2="5"/>
      <g stroke-width="1.6"><path d="M6 11h1M10 11h1M14 11h1M6 14h1M10 14h1M14 14h1M6 17h1M10 17h1M14 17h1"/></g>
    </svg>
  </div>
  <div class="field col-b row-3">Choose Session Time
    <svg class="field__icon" viewBox="0 0 21 21" fill="none" stroke="rgba(255,255,255,.55)" stroke-width="1.3" aria-hidden="true">
      <circle cx="10.5" cy="10.5" r="9.5"/><polyline points="10.5,5 10.5,10.5 13.5,13.5"/>
    </svg>
  </div>
  <div class="submit">SUBMIT NOW</div>
</main>

<footer class="footer">
  <div class="brand"><span class="brand__mark"></span>meridian ledger</div>
  <p class="footer__about">Mauris rutrum justo justo, quis vestibulum ligula facilisis id nn pellentesque.</p>
  <div class="social" aria-label="Social links">
    <svg viewBox="0 0 29 33" fill="none" stroke="var(--social-line)" stroke-width="1.3"><path d="M14.5 1 L28 8.75 V24.25 L14.5 32 L1 24.25 V8.75 Z"/><circle cx="14.5" cy="16.5" r="3" fill="var(--social-line)" stroke="none"/></svg>
    <svg viewBox="0 0 29 33" fill="none" stroke="var(--social-line)" stroke-width="1.3"><path d="M14.5 1 L28 8.75 V24.25 L14.5 32 L1 24.25 V8.75 Z"/><circle cx="14.5" cy="16.5" r="3" fill="var(--social-line)" stroke="none"/></svg>
    <svg viewBox="0 0 29 33" fill="none" stroke="var(--social-line)" stroke-width="1.3"><path d="M14.5 1 L28 8.75 V24.25 L14.5 32 L1 24.25 V8.75 Z"/><circle cx="14.5" cy="16.5" r="3" fill="var(--social-line)" stroke="none"/></svg>
    <svg viewBox="0 0 29 33" fill="none" stroke="var(--social-line)" stroke-width="1.3"><path d="M14.5 1 L28 8.75 V24.25 L14.5 32 L1 24.25 V8.75 Z"/><circle cx="14.5" cy="16.5" r="3" fill="var(--social-line)" stroke="none"/></svg>
  </div>
  <p class="copyright">2018 © Copyright Meridian Ledger. All Rights Reserved.</p>

  <nav class="links links--services"><h3>Services</h3>
    <ul><li>Lorem Ipsum dolor</li><li>Nullam in auctor</li><li>Maecenas tempus</li><li>Pellentesque in diam</li></ul></nav>
  <nav class="links links--company"><h3>Company</h3>
    <ul><li>The Team</li><li>About Us</li><li>Blog</li><li>Press</li></ul></nav>
  <nav class="links links--resources"><h3>Resources</h3>
    <ul><li>Support</li><li>Contact</li><li>Cookies</li><li>Terms of Services</li></ul></nav>
</footer>

</body>
</html>
```